Brontaro Web Site

Redesigned web site for Brontaro Ltd (www.brontaro-example.co.uk). This is to feature new logo (attached). Brontaro Ltd is a company which specialises in Geographic Information Systems and Geographic data - we call ourselves GIS Data Specialists. We are looking for something which conveys our professionalism and our experience. There will be more pages than on the current Brontaro website. There will be: Home, Data Migration, Data Cleansing & Validation, Data Analysis, Data Maintenance, Data Quality and an About Us page. All these should be accessible from each page on the website.
Updates
I didn't really think to say that the content of the web site is going to change from the current one we have. There will be more pages than on the current one. They will be: Home, Data Migration, Data Cleansing & Validation, Data Analysis, Data Maintenance, Data Quality and an About Us page. All these should be accessible from each page on the website. I didn't really think through the fact that the number of pages / areas to access can influence the layout of the site, sorry.
Target Market(s)
Utility Companies (e.g. telecommunications providers, energy companies), local government.
Industry/Entity Type
It Company
Look and feel

```html
<!DOCTYPE html>
<html lang="en">
<head>
<meta charset="utf-8">
<title>Brontaro Web Site</title>
<link rel="stylesheet" href="https://fonts.googleapis.com/css2?family=Source+Sans+3:wght@400;500&family=PT+Sans+Narrow&display=swap">
<style>
  :root {
    --mint-bg: #d3f5f1;
    --mint-deep: #5fb0a8;
    --panel-top: #c6ebe6;
    --panel-mid: #f7fdfc;
    --panel-low: #8fd8cf;
    --text-grey: #6f7573;
    --nav-active: #5b6260;
    --nav-muted: #a9bcb9;
    --logo-teal: #7fd0c6;
    --divider: #a6dcd5;
  }
  * { margin: 0; padding: 0; box-sizing: border-box; }
  html, body { width: 1200px; height: 900px; overflow: hidden; }
  body {
    position: relative;
    background: linear-gradient(to bottom, var(--mint-bg) 0%, var(--mint-bg) 74%, #a9ddd7 84%, var(--mint-deep) 100%);
    font-family: "Source Sans 3", sans-serif;
    color: var(--text-grey);
  }
  .brand {
    position: absolute;
    left: 134px;
    top: 40px;
    display: flex;
    align-items: center;
    gap: 16px;
  }
  .brand-mark {
    width: 58px; height: 58px;
    border-radius: 50%;
    background: var(--logo-teal);
  }
  .brand-name {
    font-size: 48px;
    font-weight: 500;
    color: #7d7f80;
    line-height: 1;
    letter-spacing: 0.5px;
  }
  .brand-tagline {
    display: block;
    font-size: 21px;
    font-weight: 400;
    color: #8a8c8d;
    letter-spacing: 0.3px;
    margin-top: 4px;
  }
  .panel {
    position: absolute;
    left: 132px;
    top: 170px;
    width: 936px;
    height: 730px;
    background: linear-gradient(to bottom, var(--panel-top) 0%, var(--panel-mid) 26%, var(--panel-mid) 34%, #bfe9e3 58%, var(--panel-low) 75%, #c9ece8 100%);
    box-shadow: 0 0 30px rgba(255,255,255,0.7);
  }
  .site-nav {
    position: absolute;
    left: 0;
    top: 0;
    width: 160px;
    height: 520px;
    border-right: 2px solid var(--divider);
    padding: 65px 0 0 43px;
  }
  .site-nav ul { list-style: none; }
  .site-nav li {
    font-family: "PT Sans Narrow", sans-serif;
    font-size: 14px;
    line-height: 20px;
    margin-bottom: 19px;
    color: var(--nav-muted);
  }
  .site-nav li.current { color: var(--nav-active); }
  .content {
    position: absolute;
    left: 209px;
    top: 50px;
    width: 670px;
  }
  .content h1 {
    font-size: 29px;
    font-weight: 400;
    color: #6c7371;
    margin-bottom: 8px;
  }
  .content p {
    font-size: 17.6px;
    line-height: 22.6px;
    margin-bottom: 22.6px;
  }
  .feature-art {
    position: absolute;
    left: 13px;
    top: 510px;
    width: 910px;
    height: 220px;
    background: linear-gradient(to bottom, rgba(143,216,207,0) 0%, rgba(160,222,214,0.8) 40%, #c9ece8 100%);
  }
</style>
</head>
<body>
  <header class="brand">
    <span class="brand-mark" aria-hidden="true"></span>
    <div>
      <span class="brand-name">Brontaro</span>
      <span class="brand-tagline">GIS Data Specialists</span>
    </div>
  </header>

  <main class="panel">
    <nav class="site-nav">
      <ul>
        <li class="current">Home</li>
        <li>Data Migration</li>
        <li>Data Cleaning &amp;<br>Validation</li>
        <li>Data Analysis</li>
        <li>Data Maintenance</li>
        <li>Data Quality</li>
        <li>About Us</li>
      </ul>
    </nav>

    <section class="content">
      <h1>Welcome to Brontaro</h1>
      <p>Brontaro was founded in 1994 by a group of geospatial software engineers that recognised the significant value that data, and the systems used to store and analyse this data, could bring to business.</p>
      <p>Our Customers: We have worked with over 200 companies in a myriad of market sectors - from utilities, local and central government, oil and gas, to many spheres of the marine industry.</p>
      <p>Our Pedigree: We provide a vast bank of knowledge and experience to offer an all encompassing service. This ensures that you, as a customer, reap the maximum benefits from your data and systems through utilising a combination of our skilled consultants, analysts and developers that will work with you and your requirements to help achieve your business objectives.</p>
      <p>Our People: We have a wide ranging skill set including PROVEN 2 qualified Project Managers, fully qualified Software Developers and Experienced Data Consultants.</p>
    </section>

    <div class="feature-art" role="img" aria-label="Faded illustration of database tables and account records fading into the teal background"></div>
  </main>
</body>
</html>
```